New design for www.TrimTable.com

On TrimTable you can find & book your hairdresser. TrimTable is the biggest platform in the Netherlands.

- The design should be a responcive design
- Should be able to go global, should fit in perfectly between all the big booking platforms like roomquay, zipvan etc,
- Should have te result of more bookings. :)
- We are ‘only’ asking a beautiful design, not a technical solution.
- We need a homepage (https://trimtable.com/), search resultpage ((https://trimtable.com/kapper/amsterdam/#), salonpage (https://trimtable.com/kapper/vorden/sol-mira-hair/), about us page (https://trimtable.com/aboutus/), for the hairdresser info page (https://trimtable.com/kapper/), login/register page (https://trimtable.com/account/signin/).

- On the page of the hairdresser there is a dynamic part. The part where you create your appointment. Please take a look at this part too after you choose your treatment (behandeling), employee (medewerker), Date (datum) and time (tijd). The part that you see after this, is the part where you fill in your data as a consumer.

I've added more logo's but mostly we use the green color.

A few of our competitors: www.glowpick.com, www.kestoly.com

Target Market(s)

All consumers

Industry/Entity Type

Hair And Beauty

Number of Pages Required

5+ page

Font styles to use
Sans Serif

Colors
abd036
c3c3c3
757575

Requirements
Must have
• Responsive
• We did an A/B test with the homepage. It turns out that option B works better then option A (take a look at the uploaded pictures). So what we need on the homepage: The USP's with the green checkboxes, The search button needs to by dynamic (changes for example from light green to dark green so you can see you can click it) The call to action sentence Zoek & Vind je kapsalon, the searchfield and searchbutton should be seperated.
Nice to have
• The style that we like is the flat design style. The website should be simple, clean and it should feel a bit like a luxury thing. Because an appointment with the hairdresser can be a real treat and luxury moment for yourself.
• The luxury feeling and flat design that is in the www.zipvan.com website is really nice for example. But then it has to be a bit more light and not so black and dark.

```html
<!DOCTYPE html>
<html lang="en">
<head>
<meta charset="utf-8">
<title>TrimTable – Find &amp; book your hairdresser</title>
<link rel="stylesheet" href="https://fonts.googleapis.com/css2?family=Open+Sans:wght@400;600;700&family=Raleway:wght@300;400&family=Lora:ital@0;1&display=swap">
<style>
:root{
  --green:#abd036;
  --green-dark:#8db21f;
  --grey-light:#c3c3c3;
  --grey:#757575;
  --ink:#3a3a3a;
  --dark:#2b2b2b;
  --darker:#222;
  --white:#fff;
  --red:#e0392b;
}
*{margin:0;padding:0;box-sizing:border-box}
html,body{width:682px;height:1200px;overflow:hidden}
body{font-family:"Open Sans",Arial,sans-serif;color:var(--grey);background:var(--white);position:relative}

/* hero */
.hero{position:relative;height:443px;overflow:hidden}
.hero-photo{position:absolute;inset:0;background:linear-gradient(100deg,#4a3a32 0%,#7c6a5e 30%,#b49a86 55%,#d9c7b6 75%,#8f7566 100%)}
.hero-shade{position:absolute;inset:0;background:rgba(0,0,0,.12)}
.topbar{position:absolute;top:0;left:0;right:0;height:58px;display:flex;align-items:center;justify-content:space-between;padding:0 48px 0 80px}
.brand{display:flex;align-items:center;gap:8px;color:var(--white);font-weight:700;font-size:18px;text-decoration:none}
.brand-mark{width:24px;height:24px;background:var(--green);border-radius:50%}
.nav{display:flex;gap:10px}
.nav a{color:var(--white);font-size:9px;letter-spacing:.5px;text-decoration:none;text-transform:uppercase}
.search-box{position:absolute;left:182px;top:160px;width:340px;height:130px;background:rgba(40,40,40,.55);padding:22px 26px;color:var(--white)}
.search-title{font-size:14px;letter-spacing:1px;text-transform:uppercase;font-weight:400}
.search-sub{font-size:11px;margin-top:8px;line-height:1.45;max-width:230px}
.search-form{display:flex;gap:6px;margin-top:12px}
.search-field{flex:1;height:26px;background:var(--white);border:0;font-size:9px;color:var(--grey);padding:0 10px;display:flex;align-items:center;text-transform:uppercase}
.search-btn{width:48px;height:26px;background:var(--green);display:flex;align-items:center;justify-content:center}

/* intro */
.intro{position:relative;height:204px;display:flex;padding:22px 0 0 90px;gap:26px}
.usp{width:206px;height:160px;background:var(--green);color:var(--white);padding:18px 16px}
.usp h2{font-family:"Raleway",sans-serif;font-weight:400;font-size:16px;line-height:1.3}
.usp p{font-size:7px;line-height:1.6;margin-top:10px;opacity:.9}
.intro-copy{width:300px;padding-top:6px}
.intro-copy h1{font-family:"Raleway",sans-serif;font-weight:300;font-size:20px;color:var(--green)}
.intro-copy p{font-size:7px;line-height:1.65;margin-top:10px}

/* features */
.features{height:148px;display:grid;grid-template-columns:200px 140px 150px;gap:24px;padding:8px 0 0 90px;border-top:1px solid #eee}
.features h3{font-size:9px;font-weight:600;color:var(--green-dark);margin-bottom:6px}
.award-lead{font-size:10px;color:var(--ink);line-height:1.4}
.award-text{font-size:6.5px;line-height:1.6;margin-top:8px}
.gallery{display:grid;grid-template-columns:repeat(4,1fr);gap:4px}
.gallery-tile{height:28px;background:linear-gradient(135deg,#5a4a42,#b59c8c)}
.gallery-tile:nth-child(even){background:linear-gradient(135deg,#2f2f2f,#7a6e66)}
.services{width:100%;border-collapse:collapse;font-size:7px}
.services td{border:1px solid #e3e3e3;padding:4px 5px}
.services td:last-child{text-align:right;color:var(--ink)}

/* partners */
.partners{height:102px;background:var(--dark);display:flex;flex-direction:column;align-items:center;justify-content:center;gap:14px}
.partner-row{display:flex;gap:44px}
.partner-name{color:var(--white);font-size:14px;font-weight:600;letter-spacing:1px}
.dots{display:flex;gap:4px}
.dots span{width:5px;height:5px;border-radius:50%;background:var(--grey)}
.dots span.active{background:var(--white)}

/* quote */
.quote{position:relative;height:193px;overflow:hidden}
.quote-photo{position:absolute;inset:0;background:linear-gradient(180deg,#c8c0b8 0%,#8a6e5c 55%,#4d3b31 100%)}
.quote-shade{position:absolute;inset:0;background:rgba(0,0,0,.35)}
.quote blockquote{position:relative;width:420px;margin:66px auto 0;text-align:center;color:var(--white);font-family:"Lora",Georgia,serif;font-size:15px;line-height:1.35}
.quote cite{display:block;font-size:11px;font-style:italic;color:var(--green);margin-top:2px}

/* footer */
.footer{height:110px;background:var(--darker);text-align:center;padding-top:12px;position:relative}
.footer-text{width:460px;margin:0 auto;font-size:6.5px;line-height:1.6;font-style:italic;color:#8a8a8a}
.social{display:flex;justify-content:center;gap:22px;margin-top:12px}
.social span{width:14px;height:14px;border-radius:50%;background:var(--grey)}
.copyright{font-size:6px;color:var(--grey);margin-top:10px}
.to-top{position:absolute;right:22px;bottom:14px;width:16px;height:16px;border-radius:50%;background:var(--red);display:flex;align-items:center;justify-content:center}
</style>
</head>
<body>

<header class="hero">
  <div class="hero-photo" role="img" aria-label="Photo of a hairdresser styling a young woman's hair in a salon"></div>
  <div class="hero-shade"></div>
  <div class="topbar">
    <a class="brand" href="https://trimtable.com/"><span class="brand-mark"></span>TrimTable</a>
    <nav class="nav"><a href="https://trimtable.com/account/signin/">Login</a><a href="https://trimtable.com/account/signin/">Register</a></nav>
  </div>
  <div class="search-box">
    <p class="search-title">Lorem is is a dummy text</p>
    <p class="search-sub">On TrimTable you can find &amp; book your hairdresser.</p>
    <div class="search-form">
      <div class="search-field">Looking for</div>
      <div class="search-btn">
        <svg width="14" height="10" viewBox="0 0 14 10"><path d="M1 2h3M1 8h3M6 2h7M6 8h7M4 0v4M4 6v4" stroke="#fff" stroke-width="1.4" fill="none"/></svg>
      </div>
    </div>
  </div>
</header>

<section class="intro">
  <div class="usp">
    <h2>Haircuts, facial waxing, and beard trims</h2>
    <p>Book a trusted stylist near you in seconds. Compare salons, read honest reviews and choose the time that suits your day. Treat yourself today.</p>
  </div>
  <div class="intro-copy">
    <h1>Enjoy Your Haircut Again</h1>
    <p>Every visit to the salon should feel like a small luxury. With TrimTable you browse hundreds of salons, compare treatments and prices, and reserve your chair without a single phone call. Your favourite stylist is only a few clicks away.</p>
    <p>Choose your treatment, pick an employee you trust and select a date and time that fits. We send a friendly reminder before your appointment, so you can simply relax and enjoy the moment. Rebooking takes one tap, and every review helps others find their perfect salon in town.</p>
  </div>
</section>

<section class="features">
  <div>
    <h3>Award Winning Stai</h3>
    <p class="award-lead">Cras justo odio, dapibus ac facilisis in, egestas eget quam. Maecenas sed diam eget.</p>
    <p class="award-text">Our partner salons are chosen for skill, care and service. Each stylist is reviewed by real guests, so you always know what to expect before you book your next visit with us.</p>
  </div>
  <div>
    <h3>Works by Stylist</h3>
    <div class="gallery" role="img" aria-label="Grid of photos showing finished haircuts and styling tools">
      <span class="gallery-tile"></span><span class="gallery-tile"></span><span class="gallery-tile"></span><span class="gallery-tile"></span>
      <span class="gallery-tile"></span><span class="gallery-tile"></span><span class="gallery-tile"></span><span class="gallery-tile"></span>
    </div>
  </div>
  <div>
    <h3>Our Services</h3>
    <table class="services">
      <tr><td>Haircut</td><td>€ 25</td></tr>
      <tr><td>Beard trim</td><td>€ 15</td></tr>
      <tr><td>Facial waxing</td><td>€ 20</td></tr>
      <tr><td>Colour &amp; styling</td><td>€ 45</td></tr>
    </table>
  </div>
</section>

<section class="partners">
  <div class="partner-row">
    <span class="partner-name">RIVANE</span>
    <span class="partner-name">BLUMARK</span>
    <span class="partner-name">SOMERA</span>
    <span class="partner-name">LUMIERA</span>
    <span class="partner-name">WENNA</span>
    <span class="partner-name">Schorla</span>
  </div>
  <div class="dots"><span class="active"></span><span></span></div>
</section>

<section class="quote">
  <div class="quote-photo" role="img" aria-label="Soft-focus photo of a salon interior"></div>
  <div class="quote-shade"></div>
  <blockquote>I think that the most important thing a woman can have - next to talent, of course - is her hairdresser.<cite>– Mara Velden –</cite></blockquote>
</section>

<footer class="footer">
  <p class="footer-text">TrimTable helps you find and book the best hairdressers near you. Browse salons, compare treatments and prices, read genuine reviews and reserve your appointment online at any hour. Simple, quick and always free for guests across the whole country.</p>
  <div class="social"><span></span><span></span><span></span></div>
  <p class="copyright">TrimTable 2016 © All rights reserved</p>
  <div class="to-top"><svg width="8" height="6" viewBox="0 0 8 6"><path d="M1 5l3-3 3 3" stroke="#fff" stroke-width="1.4" fill="none"/></svg></div>
</footer>

</body>
</html>
```